Quarnfield Fintech Product Infographic

Quarnfield is an established Fintech business, supplying complex financial software to banks and building societies.

We currently have a picture/infographic to show each of our 11 different software products in a single image. Each product can be installed on its own as a standalone application or if multiple products are installed they will share data.

The key message for our infographic is to convey the integration via a shared database.

The attached diagram is what we currently use which is to give you an idea of the message we are trying to give, but we are not tied to this format and are looking for this diagram to be reimagined.

We will look to use our new chosen design on printed media such as A4 Data sheets an example of which is attached.

For more information on our products please refer to www.quarnfield-example.co.uk/products

```html
<!DOCTYPE html>
<html lang="en">
<head>
<meta charset="utf-8">
<title>Quarnfield Product Suite – Shared Data</title>
<link href="https://fonts.googleapis.com/css2?family=Mulish:wght@500;600;700;800&display=swap" rel="stylesheet">
<style>
  :root {
    --bg: #ffffff;
    --ledgers: #2394c2;
    --eir: #36a9dc;
    --hedge: #4dbbeb;
    --regrep: #2aa55c;
    --taxrep: #4fb577;
    --fscs: #6ac28f;
    --alm: #e99637;
    --treasury: #fdbb4e;
    --bi: #a55294;
    --ftp: #b669a8;
    --planning: #c07ab4;
    --finance: #3fb0e3;
    --performance: #b86aa8;
    --regulatory: #5cbf83;
    --risk: #fbb33f;
    --finance-arc: #d9eef9;
    --performance-arc: #efdcec;
    --regulatory-arc: #cfe9d9;
    --risk-arc: #fdebc8;
    --connector: #d3d3d3;
    --ring: #e4e4e4;
    --hub-text: #2d3a7c;
  }
  html, body { margin: 0; padding: 0; overflow: hidden; background: var(--bg); }
  .canvas { width: 1200px; height: 849px; position: relative; }
  .diagram { display: block; font-family: "Mulish", sans-serif; }
  .product-label { fill: #fff; font-size: 19px; font-weight: 600; text-anchor: middle; }
  .group-label { font-size: 21px; font-weight: 700; letter-spacing: 2px; text-anchor: middle; }
  .group-arc { fill: none; stroke-width: 3; stroke-linecap: round; }
  .connector { stroke: var(--connector); stroke-width: 5.5; stroke-linecap: round; stroke-dasharray: 0 1; fill: none; }
  .node-ring { fill: #fff; stroke-width: 1.6; }
  .hub-label { fill: var(--hub-text); font-size: 15px; font-weight: 800; text-anchor: middle; }
</style>
</head>
<body>
<div class="canvas">
<svg class="diagram" width="1200" height="849" viewBox="0 0 1200 849" xmlns="http://www.w3.org/2000/svg">
  <defs>
    <filter id="soft-shadow" x="-30%" y="-30%" width="160%" height="160%">
      <feDropShadow dx="3" dy="6" stdDeviation="7" flood-color="#000" flood-opacity="0.12"/>
    </filter>
    <linearGradient id="servers-fill" x1="0" y1="0" x2="1" y2="1">
      <stop offset="0" stop-color="#6f7fd6"/>
      <stop offset="1" stop-color="#3b3f9e"/>
    </linearGradient>
  </defs>

  <!-- group arcs -->
  <path class="group-arc" stroke="var(--finance-arc)" d="M394 117 A368 368 0 0 1 543 57"/>
  <path class="group-arc" stroke="var(--finance-arc)" d="M660 57 A368 368 0 0 1 808 117"/>
  <path class="group-arc" stroke="var(--performance-arc)" d="M270 272 A368 368 0 0 0 235 385"/>
  <path class="group-arc" stroke="var(--performance-arc)" d="M267 575 A368 368 0 0 0 334 680"/>
  <path class="group-arc" stroke="var(--regulatory-arc)" d="M932 272 A368 368 0 0 1 968 395"/>
  <path class="group-arc" stroke="var(--regulatory-arc)" d="M942 560 A368 368 0 0 1 869 680"/>
  <path class="group-arc" stroke="var(--risk-arc)" d="M494 775 A368 368 0 0 0 563 787"/>
  <path class="group-arc" stroke="var(--risk-arc)" d="M639 787 A368 368 0 0 0 708 775"/>

  <text class="group-label" x="601" y="70" fill="var(--finance)">FINANCE</text>
  <text class="group-label" x="601" y="798" fill="var(--risk)">RISK</text>
  <text class="group-label" fill="var(--performance)" transform="translate(239 482) rotate(90)">PERFORMANCE</text>
  <text class="group-label" fill="var(--regulatory)" transform="translate(971 474) rotate(-90)">REGULATORY</text>

  <!-- inner ring -->
  <circle cx="601" cy="421" r="117" fill="none" stroke="var(--ring)" stroke-width="2.5"/>

  <!-- connectors -->
  <line class="connector" pathLength="2" x1="503" y1="272" x2="521" y2="300"/>
  <line class="connector" pathLength="2" x1="601" y1="243" x2="601" y2="277"/>
  <line class="connector" pathLength="2" x1="699" y1="272" x2="681" y2="300"/>
  <line class="connector" pathLength="2" x1="767" y1="349" x2="735" y2="363"/>
  <line class="connector" pathLength="2" x1="782" y1="450" x2="747" y2="446"/>
  <line class="connector" pathLength="2" x1="739" y1="544" x2="713" y2="521"/>
  <line class="connector" pathLength="2" x1="653" y1="599" x2="643" y2="566"/>
  <line class="connector" pathLength="2" x1="550" y1="599" x2="560" y2="566"/>
  <line class="connector" pathLength="2" x1="464" y1="544" x2="490" y2="521"/>
  <line class="connector" pathLength="2" x1="421" y1="450" x2="455" y2="446"/>
  <line class="connector" pathLength="2" x1="435" y1="349" x2="467" y2="363"/>

  <!-- ring nodes -->
  <g class="nodes">
    <circle class="node-ring" cx="539" cy="328" r="16" stroke="var(--ledgers)"/><circle cx="539" cy="328" r="6" fill="var(--ledgers)"/>
    <circle class="node-ring" cx="601" cy="309" r="16" stroke="var(--eir)"/><circle cx="601" cy="309" r="6" fill="var(--eir)"/>
    <circle class="node-ring" cx="664" cy="328" r="16" stroke="var(--hedge)"/><circle cx="664" cy="328" r="6" fill="var(--hedge)"/>
    <circle class="node-ring" cx="707" cy="376" r="16" stroke="var(--regrep)"/><circle cx="707" cy="376" r="6" fill="var(--regrep)"/>
    <circle class="node-ring" cx="716" cy="442" r="16" stroke="var(--taxrep)"/><circle cx="716" cy="442" r="6" fill="var(--taxrep)"/>
    <circle class="node-ring" cx="689" cy="501" r="16" stroke="var(--fscs)"/><circle cx="689" cy="501" r="6" fill="var(--fscs)"/>
    <circle class="node-ring" cx="634" cy="536" r="16" stroke="var(--alm)"/><circle cx="634" cy="536" r="6" fill="var(--alm)"/>
    <circle class="node-ring" cx="568" cy="536" r="16" stroke="var(--treasury)"/><circle cx="568" cy="536" r="6" fill="var(--treasury)"/>
    <circle class="node-ring" cx="514" cy="501" r="16" stroke="var(--bi)"/><circle cx="514" cy="501" r="6" fill="var(--bi)"/>
    <circle class="node-ring" cx="486" cy="442" r="16" stroke="var(--ftp)"/><circle cx="486" cy="442" r="6" fill="var(--ftp)"/>
    <circle class="node-ring" cx="496" cy="376" r="16" stroke="var(--planning)"/><circle cx="496" cy="376" r="6" fill="var(--planning)"/>
  </g>

  <!-- hub -->
  <circle cx="601" cy="421" r="79" fill="#fff" filter="url(#soft-shadow)"/>
  <rect x="556" y="370" width="90" height="62" rx="8" fill="url(#servers-fill)" opacity="0.85" role="img" aria-label="Illustration of database servers"/>
  <text class="hub-label" x="601" y="469">SHARED DATA</text>

  <!-- products -->
  <g class="products" filter="url(#soft-shadow)">
    <circle cx="461" cy="206" r="63" fill="var(--ledgers)"/>
    <circle cx="601" cy="165" r="63" fill="var(--eir)"/>
    <circle cx="742" cy="206" r="63" fill="var(--hedge)"/>
    <circle cx="838" cy="317" r="63" fill="var(--regrep)"/>
    <circle cx="859" cy="461" r="63" fill="var(--taxrep)"/>
    <circle cx="797" cy="595" r="63" fill="var(--fscs)"/>
    <circle cx="674" cy="675" r="63" fill="var(--alm)"/>
    <circle cx="528" cy="675" r="63" fill="var(--treasury)"/>
    <circle cx="405" cy="595" r="63" fill="var(--bi)"/>
    <circle cx="344" cy="461" r="63" fill="var(--ftp)"/>
    <circle cx="365" cy="317" r="63" fill="var(--planning)"/>
  </g>

  <text class="product-label" x="461" y="205">Financial<tspan x="461" dy="19">Ledgers</tspan></text>
  <text class="product-label" x="601" y="154">Effective<tspan x="601" dy="19">Interest</tspan><tspan x="601" dy="19">Rates</tspan></text>
  <text class="product-label" x="742" y="202">Hedge<tspan x="742" dy="19">Accounting</tspan></text>
  <text class="product-label" x="838" y="316">Regulatory<tspan x="838" dy="19">Reporting</tspan></text>
  <text class="product-label" x="860" y="458">Taxation<tspan x="860" dy="19">Reporting</tspan></text>
  <text class="product-label" x="797" y="595">FSCS<tspan x="797" dy="19">SCV</tspan></text>
  <text class="product-label" x="672" y="685">ALM</text>
  <text class="product-label" x="528" y="685">Treasury</text>
  <text class="product-label" x="407" y="595">Business<tspan x="407" dy="19">Intelligence</tspan></text>
  <text class="product-label" x="343" y="451">Funds<tspan x="343" dy="19">Transfer</tspan><tspan x="343" dy="19">Pricing</tspan></text>
  <text class="product-label" x="367" y="316">Financial<tspan x="367" dy="19">Planning</tspan></text>
</svg>
</div>
</body>
</html>
```